2 sided postcard for New Internet Customers

We would like a design for a two sided postcard (with room for mailing label), dimensions 9 1/4 by 6 1/4 to be sent via US Mail.

The postcard needs to include our logo (attached) and the text
Fiber Optic Internet
555-219-8063
http://www.brightwirenet.example
Speeds up to 1 Gig, with packages starting at $55

These will be sent to people who do not have our service.

Since this is going to be "junk mail" we probably only have 1 second or less to capture someone's attention to encourage them to read the entire postcard.

We are a "mom and pop" telecommunications company that provides internet, phone, and television services on the fiber optic network that we designed, built, and maintain.

We started as a dial up ISP in 1995, and have extraordinary technical support based in Freeport PA, our customers actually get the speeds they pay for, and our service is highly reliable.

We have a slogan (which you can choose to use or ignore) which is
"I Went Fast with Kornwell"

Existing customers can earn a $50 credit for every new customer they refer to us. Unlike most large cable and internet companies we have very happy customers... some who have stayed with us for decades.

I've attached our previous postcard, which I really dislike. It does have a blank spot for where the mailing label should go.

Target Market(s)

New Internet Customers in Western Pennsylvania

Industry/Entity Type

Internet

Font styles to use
Other font styles liked:
• Just match our logo.

Colors

Designer to choose colors to be used in the design.

Requirements
Must have
• The postcard needs to include our logo, and the text Fiber Optic Internet 555-219-8063 http://www.brightwirenet.example Speeds up to 1 Gig, with packages starting at $55
Nice to have
• The colors and fonts should look good with our logo.
Should not have
• Should not have small print or lots of text. Both sides need to capture attention.

```html
<!DOCTYPE html>
<html lang="en">
<head>
<meta charset="utf-8">
<title>Kornwell Fiber Postcard</title>
<link rel="stylesheet" href="https://fonts.googleapis.com/css2?family=Bebas+Neue&family=Montserrat:wght@500;600;700;800&display=swap">
<style>
:root{
  --stage:#d3ccc0;
  --navy:#0b1330;
  --deep:#16306e;
  --brand:#0f74c4;
  --brand-bright:#1c7fd0;
  --arch:#1559b2;
  --white:#ffffff;
  --label:#e3e3e3;
}
*{box-sizing:border-box;margin:0;padding:0}
html,body{width:921px;height:1200px;overflow:hidden;background:var(--stage);font-family:"Montserrat",sans-serif}
.card{position:absolute;left:81px;width:760px;height:506px;overflow:hidden;background:var(--white)}
.card--front{top:76px}
.card--back{top:618px}
.backdrop{position:absolute;inset:0;background:
  radial-gradient(ellipse 70% 35% at 75% 52%,rgba(120,180,255,.45),transparent 70%),
  linear-gradient(180deg,var(--navy) 0%,var(--deep) 48%,#1a63bd 80%,#1b6fca 100%)}
.card--back .backdrop{height:296px;background:
  radial-gradient(ellipse 60% 30% at 45% 70%,rgba(120,180,255,.4),transparent 70%),
  linear-gradient(180deg,var(--navy) 0%,var(--deep) 45%,#1a63bd 85%,#1b6fca 100%)}
.brand{position:absolute;left:32px;top:31px;display:flex;align-items:flex-end}
.brand__mark{width:64px;height:64px;border-radius:50%;background:var(--brand-bright)}
.brand__name{margin-left:11px;margin-bottom:1px;height:26px;padding:0 13px;border-radius:13px;background:var(--brand-bright);color:var(--white);font-weight:500;font-size:17px;line-height:26px;white-space:nowrap}
.headline{position:absolute;left:34px;font-weight:800;font-size:79px;line-height:1;letter-spacing:-.5px}
.headline--white{top:112px;color:var(--white)}
.headline--blue{top:188px;color:var(--brand)}
.slogan{position:absolute;left:0;top:270px;width:387px;height:42px;border-radius:0 21px 21px 0;background:var(--brand-bright);color:var(--white);font-weight:600;font-size:25px;line-height:42px;padding-left:37px;white-space:nowrap}
.referral{position:absolute;left:0;top:305px;width:435px;height:104px;border-radius:0 52px 52px 0;background:rgba(40,110,210,.55);padding:19px 0 0 35px}
.referral p{width:381px;color:var(--white);font-weight:600;font-size:12.6px;line-height:19.5px;text-align:justify}
.contact{position:absolute;left:0;top:409px;width:482px;height:97px;background:linear-gradient(180deg,#1569c0,#1776c8)}
.contact__phone{position:absolute;left:27px;top:8px;color:var(--white);font-weight:700;font-size:50px;line-height:1;letter-spacing:.5px}
.contact__web{position:absolute;left:27px;top:60px;color:var(--white);font-weight:700;font-size:18px}
.offer{position:absolute;left:483px;top:243px;width:251px;height:263px;border-radius:126px 126px 0 0;background:linear-gradient(180deg,#1e66c4,var(--arch) 60%,#1452a8);text-align:center;color:var(--white);font-family:"Bebas Neue",sans-serif}
.offer__lead{margin-top:36px;font-size:31px;line-height:30px}
.offer__price{font-size:146px;line-height:1;margin-top:2px}
.section-title{position:absolute;left:33px;top:129px;color:var(--brand-bright);font-weight:800;font-size:29px;white-space:nowrap}
.benefits{position:absolute;left:32px;top:168px;list-style:none;color:var(--white);font-weight:700;font-size:29px;line-height:37px}
.connectors{position:absolute;left:440px;top:0;width:320px;height:265px;background:radial-gradient(ellipse 60% 45% at 55% 55%,rgba(60,110,220,.8),rgba(30,70,170,.2) 70%,transparent)}
.mailing{position:absolute;left:0;top:396px;width:760px;text-align:center;color:var(--label);font-size:12px;letter-spacing:17px;font-weight:500}
</style>
</head>
<body>
<section class="card card--front">
  <div class="backdrop" role="img" aria-label="Glowing blue fiber optic light streaks on a dark navy background"></div>
  <div class="brand"><div class="brand__mark"></div><div class="brand__name">Kornwell Internet Services</div></div>
  <h1 class="headline headline--white">FIBER OPTIC</h1>
  <h2 class="headline headline--blue">INTERNET</h2>
  <div class="slogan">I WENT FAST WITH KORNWELL</div>
  <div class="referral"><p>Existing customers can earn a $50 credit for every new customer they refer to us. Unlike most large cable and internet companies we have very happy customers... some who have stayed with us for decades.</p></div>
  <div class="contact">
    <div class="contact__phone">555-219-8063</div>
    <div class="contact__web">www.brightwirenet.example</div>
  </div>
  <div class="offer">
    <p class="offer__lead">SPEEDS UP TO<br>1 GIG WITH PACKAGES<br>STARTING AT</p>
    <p class="offer__price">$55</p>
  </div>
</section>
<section class="card card--back">
  <div class="backdrop" role="img" aria-label="Blue fiber optic light streaks over a dark navy background"></div>
  <div class="connectors" role="img" aria-label="Blue fiber optic cable connectors on yellow cables"></div>
  <div class="brand"><div class="brand__mark"></div><div class="brand__name">Kornwell Internet Services</div></div>
  <h2 class="section-title">FIBER IS THE BEST FOR:</h2>
  <ul class="benefits"><li>Streaming</li><li>Gaming</li><li>Reliability</li></ul>
  <p class="mailing">MAILING ADDRESS</p>
</section>
</body>
</html>
```